Create a customised branding Information Memorandum Document

Our business is harlowmintco.com.au
Our key document is an Information Memorandum. We need a completely fresh approach to this document incorporating our new brand (logos are attached in this brief). The document we need delivered is approximately 60 pages. We need a master template created that can then be regularly customised to promote different businesses that we are selling. The document has to be easily customised but must be fresh and contemporary. We are currently undergoing a website revamp. We are drawing inspiration for the new website from quillorchid.com.au This website is not in the same industry, but it conveys the vibe that we are going for. Our company specialises in business sales. The document must be fresh, but also professional and corporate. I have shared a few first sample pages. When we see design options and appoint a designer, we will share the whole document.

```html
<!DOCTYPE html>
<html lang="en">
<head>
<meta charset="utf-8">
<title>Harlow Mint Co – Information Memorandum</title>
<link rel="stylesheet" href="https://fonts.googleapis.com/css2?family=Poppins:wght@400;500;600&display=swap">
<style>
  :root{
    --bg:#b4c2cc;
    --paper:#f4f4f4;
    --paper-shade:#e9e9e9;
    --maroon:#9c2f40;
    --ink:#2c2c30;
    --rule:#3a3a3e;
    --plum:#4e2549;
    --violet:#6d2d66;
    --pink:#c23f8e;
    --grey-photo:#bfc3c7;
  }
  *{margin:0;padding:0;box-sizing:border-box}
  html,body{width:1200px;height:800px;overflow:hidden}
  body{background:var(--bg);font-family:"Poppins",sans-serif;color:var(--ink);position:relative}

  .page{position:absolute;top:146px;width:360px;height:509px;background:var(--paper);overflow:hidden}
  .page--left{left:40px;background:linear-gradient(90deg,var(--paper) 85%,var(--paper-shade))}
  .page--right{left:400px;background:linear-gradient(90deg,var(--paper-shade),var(--paper) 12%)}
  .page--cover{left:800px;background:#f6f6f6;box-shadow:0 8px 20px rgba(40,50,60,.25)}

  .side-url{position:absolute;top:22px;right:14px;writing-mode:vertical-rl;font-size:6px;color:#777;letter-spacing:.3px}

  .brand{position:absolute;left:30px;top:110px;color:var(--maroon);font-weight:500;font-size:25px;letter-spacing:1px}
  .intro{position:absolute;left:46px;top:200px;width:200px;font-size:9px;line-height:1.6;color:var(--ink)}
  .photo-team{position:absolute;left:80px;top:350px;width:280px;height:140px;background:linear-gradient(180deg,#e3e5e7,var(--grey-photo) 55%,#6f7378)}
  .footer-tag{position:absolute;left:240px;top:484px;width:120px;height:14px;background:var(--maroon);color:#fff;font-size:5.5px;line-height:14px;padding-left:6px}

  .proposal-title{position:absolute;left:30px;top:30px;color:var(--maroon);font-size:15px;font-weight:500;font-variant:small-caps;letter-spacing:.5px}
  .proposal-title::after{content:"";position:absolute;left:0;top:26px;width:200px;height:1.5px;background:var(--rule)}
  .toc{position:absolute;top:82px;list-style:none}
  .toc--a{left:30px}.toc--b{left:236px}
  .toc li{position:relative;height:30px;width:160px;font-size:7.5px;font-weight:500;padding-left:16px;line-height:12px}
  .toc li::before{content:"";position:absolute;left:0;top:1px;width:10px;height:10px;background:var(--maroon);border-radius:2px}
  .toc li::after{content:"";position:absolute;left:24px;top:18px;width:136px;height:1px;background:var(--rule)}
  .photo-deal{position:absolute;left:0;top:380px;width:360px;height:129px;background:linear-gradient(180deg,rgba(244,244,244,0),#b9bec4 40%,#8d949b)}

  .cover-photo{position:absolute;inset:0 0 120px 0;background:linear-gradient(160deg,#7b6a80 0%,var(--violet) 35%,var(--plum) 70%,#3a2038 100%)}
  .cover-brand{position:absolute;left:0;right:0;top:70px;text-align:center;color:#fff;font-size:21px;font-weight:500;letter-spacing:1px}
  .cover-date{position:absolute;left:0;right:0;top:170px;text-align:center;color:#fff;font-size:12px;font-weight:500}
  .cover-title{position:absolute;left:0;right:0;top:186px;text-align:center;color:#fff;font-size:40px;font-weight:500;letter-spacing:1px}
  .cover-sub{position:absolute;left:0;right:0;top:240px;text-align:center;color:#fff;font-size:11.5px;font-weight:500}
  .cover-wave{position:absolute;left:0;top:300px;width:360px;height:209px}
  .presented{position:absolute;left:0;right:0;top:420px;text-align:center;font-size:7px}
  .presenter{position:absolute;left:125px;top:432px;width:110px;height:24px;border-radius:12px;background:linear-gradient(90deg,#5a5158,#7e5a6c);color:#fff;font-size:11px;font-weight:500;text-align:center;line-height:24px}
  .presenter-line{position:absolute;top:444px;height:1px;width:90px;background:var(--rule)}
  .contacts{position:absolute;left:0;right:0;top:472px;text-align:center;font-size:7px;display:flex;justify-content:center;gap:8px;align-items:center}
  .contacts svg{width:7px;height:7px;margin-right:3px;vertical-align:-1px}
</style>
</head>
<body>
  <section class="page page--left">
    <div class="brand">Harlow Mint Co</div>
    <p class="intro">Leading business sales in Canberra. We empower entrepreneurs and businesses to achieve their full potential through strategic partnerships, seamless transitions, and long-term success.</p>
    <div class="photo-team" role="img" aria-label="Photo of a cheering business team in an office"></div>
    <div class="footer-tag">Confidential - Sales Overview | 02</div>
    <span class="side-url">harlowmintco.com.au</span>
  </section>

  <section class="page page--right">
    <h2 class="proposal-title">Proposal</h2>
    <ul class="toc toc--a">
      <li>Lorem ipsum</li><li>Lorem ipsum</li><li>Lorem ipsum</li><li>Lorem ipsum</li><li>Lorem ipsum</li><li>Lorem ipsum</li><li>Lorem ipsum</li><li>Lorem ipsum</li><li>Lorem ipsum</li><li>Lorem ipsum</li><li>Lorem ipsum</li>
    </ul>
    <ul class="toc toc--b">
      <li>Lorem ipsum</li><li>Lorem ipsum</li><li>Lorem ipsum</li><li>Lorem ipsum</li><li>Lorem ipsum</li><li>Lorem ipsum</li><li>Lorem ipsum</li><li>Lorem ipsum</li><li>Lorem ipsum</li><li>Lorem ipsum</li><li>Lorem ipsum</li>
    </ul>
    <div class="photo-deal" role="img" aria-label="Photo of a handshake over a city skyline"></div>
    <span class="side-url">harlowmintco.com.au</span>
  </section>

  <section class="page page--cover">
    <div class="cover-photo" role="img" aria-label="Photo of a businessman climbing a staircase, tinted purple"></div>
    <div class="cover-brand">Harlow Mint Co</div>
    <div class="cover-date">OCTOBER 2023</div>
    <h1 class="cover-title">CONFIDENTIAL</h1>
    <div class="cover-sub">INFORMATION MEMORANDUM</div>
    <svg class="cover-wave" viewBox="0 0 360 209" preserveAspectRatio="none" aria-hidden="true">
      <path d="M0 70 C60 30 150 20 200 60 C230 85 215 120 240 135 C280 150 320 110 360 95 L360 209 L0 209 Z" fill="#f6f6f6"/>
      <path d="M120 40 C170 20 220 40 225 80 C228 110 225 125 240 135 C205 125 215 90 200 70 C185 50 150 42 120 40 Z" fill="#c23f8e"/>
      <path d="M0 70 C60 30 150 20 200 60" fill="none" stroke="#fff" stroke-width="1"/>
    </svg>
    <div class="presented">Presented by</div>
    <span class="presenter-line" style="left:30px"></span>
    <div class="presenter">MAREN HOLT</div>
    <span class="presenter-line" style="left:240px"></span>
    <div class="contacts">
      <span><svg viewBox="0 0 10 10"><rect x="0" y="2" width="10" height="6" fill="#9c2f40"/><path d="M0 2 L5 6 L10 2" stroke="#fff" fill="none"/></svg>maren@harlowmintco.com.au</span>|
      <span><svg viewBox="0 0 10 10"><rect x="2" y="0" width="6" height="10" rx="1" fill="#9c2f40"/></svg>0400 317 962</span>|
      <span><svg viewBox="0 0 10 10"><circle cx="5" cy="4" r="3.5" fill="#9c2f40"/><path d="M2 6 L5 10 L8 6Z" fill="#9c2f40"/></svg>harlowmintco.com.au</span>
    </div>
  </section>
</body>
</html>
```